2020 Texas RVN Summit Event flyer for annual conference held in Plainsview County

The Power of Connection

I need a flyer to send out via email. I The flyer will depict our theme, "The Power of Connection" event dates, website and costs. Association is Texas RVN, date April 23-25, 2020, website www.texasrvn.example, Early Bird and Member discounts location Harbor Lodge, Plainsview County

page 2 will have sponsor info, and keynote description, can be 3 pages if absolutely necessary
: keynote speaker Martin Dorsey, Martin is a retired Coastal Roadway Patrol officer who spent more than 17 years patrolling the Silver Cove Bridge. During that time he encountered hundreds of people who were troubled and had lost hope. They were ready to jump off the bridge and end their lives. Although a trained negotiator, Dorsey also relied on his compassion, gentle voice, eye contact, and his innate ability to “listening to understand”. During his career, he encouraged more than 200 people not to jump, go over the bridge’s rail or come back to solid ground from where they had been standing precariously. These challenging, but rewarding efforts earned him the nickname, “Keeper of the Silver Cove Bridge”. Retired, Dorsey is now dedicating his life to promoting mental health awareness and suicide prevention across the globe.
Great sponsor opportunities available at www.Texasrvn.example sponsor letter attached for info on sponsor opportunities it is not necessary to include all info

i attached a mockup page 1 flyer that i really like but graphic designer did not complete this would give you an idea of what i am looking for on page 1 although it is missing a few elements

the Meridale (logo attached) is a champion sponsor, Plainsview VTO (logo attached)

Target Market(s)

law enforcement, hospitals, mental health providers, court system,

Colors

Designer to choose colors to be used in the design.

Requirements
Must have
• theme -The Power of Connection
• website
• dates
• location
• costs
Nice to have
• prefer graphic related to theme
• Meridale is a large sponsor
• need to have 2-3 pages for all info
• include info on sponsor opportunities but does not have to include all info on attachment

```html
<!DOCTYPE html>
<html lang="en">
<head>
<meta charset="utf-8">
<title>2020 Texas RVN Summit – The Power of Connection</title>
<link href="https://fonts.googleapis.com/css2?family=Barlow+Semi+Condensed:wght@300;400;500;600;700&family=Roboto:wght@400;500;700&display=swap" rel="stylesheet">
<style>
:root{
  --canvas:#d6d6d6;
  --red:#e11f26;
  --red-dark:#b3141a;
  --navy:#1c2a8c;
  --navy-deep:#16236f;
  --ink:#1b1b1b;
  --text-gray:#3d3d3d;
  --card:#efefef;
  --card-edge:#e2e2e2;
  --white:#ffffff;
  --head:"Barlow Semi Condensed",sans-serif;
  --body:"Roboto",sans-serif;
}
*{box-sizing:border-box;margin:0;padding:0}
html,body{width:1200px;height:3062px;overflow:hidden;background:var(--canvas)}
.page{position:absolute;left:100px;width:1000px;height:1414px;overflow:hidden;box-shadow:0 10px 30px rgba(0,0,0,.25)}
.cover{top:78px;background:linear-gradient(180deg,#1f3440 0%,#0f1a21 35%,#05090c 60%,#0c151b 100%);color:var(--white);font-family:var(--head)}
.sponsor-sheet{top:1570px;background:var(--white);font-family:var(--body);color:var(--ink)}

/* cover */
.brand-seal{position:absolute;left:388px;top:75px;width:224px;height:224px;border-radius:50%;background:var(--white);border:10px solid var(--navy);display:flex;align-items:center;justify-content:center;font-family:var(--head);font-weight:700;font-size:40px;color:var(--navy)}
.theme-line{position:absolute;left:101px;font-weight:700;line-height:1;white-space:nowrap}
.theme-power{top:310px;font-size:136px;letter-spacing:1px}
.theme-power .of{font-size:64px;font-weight:500;margin-left:14px}
.theme-connection{top:438px;font-size:114px;color:var(--red);letter-spacing:1px}
.event-name{position:absolute;left:101px;top:552px;font-size:62px;font-weight:400;line-height:1;letter-spacing:.5px;white-space:nowrap}
.event-dates{position:absolute;left:97px;top:618px;font-size:122px;font-weight:300;line-height:1;letter-spacing:1px;white-space:nowrap}
.year-tab{position:absolute;left:781px;top:456px;width:119px;height:262px;background:var(--red);display:flex;align-items:center;justify-content:center}
.year-tab span{transform:rotate(-90deg);font-size:108px;font-weight:700;line-height:1;letter-spacing:2px}
.event-venue{position:absolute;left:0;width:1000px;text-align:center;font-size:28px;font-weight:400;letter-spacing:.3px;white-space:nowrap}
.venue-line{top:742px}
.venue-city{top:787px}
.theme-art{position:absolute;left:0;top:840px;width:1000px;height:450px}
.sponsor-marks{position:absolute;top:1272px;left:0;width:1000px;display:flex;justify-content:center;gap:90px;align-items:center}
.sponsor-mark{display:flex;align-items:center;gap:10px;font-family:var(--head);font-weight:600;font-size:32px;color:var(--white)}
.sponsor-mark .dot{width:22px;height:22px;background:#1c8f3c}
.sponsor-mark.gold{color:#c9a24a}
.cover-url{position:absolute;top:1330px;left:0;width:1000px;text-align:center;font-family:var(--body);font-size:26px;letter-spacing:.5px;color:#e8e8e8}

/* sponsor sheet */
.top-photo{position:absolute;right:0;top:0;width:500px;height:430px}
.champion-title{position:absolute;left:52px;top:41px;width:471px;height:71px;background:var(--navy);border-radius:14px 0 0 14px;color:var(--white);font-family:var(--head);font-weight:600;font-size:52px;line-height:71px;padding-left:22px;letter-spacing:.5px}
.perk-list{list-style:none}
.perk-list li{position:relative;padding-left:22px}
.perk-list li::before{content:"";position:absolute;left:0;top:2px;width:12px;height:12px;border:1.6px solid currentColor;border-radius:50%}
.perk-list li::after{content:"";position:absolute;left:4px;top:4px;width:4px;height:7px;border:solid currentColor;border-width:0 1.6px 1.6px 0;transform:rotate(40deg)}
.champion-perks{position:absolute;left:62px;top:143px;font-size:14px;font-weight:700;line-height:17px}
.champion-perks li{margin-bottom:10px;padding-left:30px}
.champion-perks li::before,.champion-perks li::after{color:var(--red)}
.champion-perks .presented{position:absolute;left:386px;top:0;white-space:nowrap}

.tier{position:absolute;background:linear-gradient(180deg,var(--card) 0%,#f6f6f6 100%);border:1px solid var(--card-edge)}
.tier-head{background:var(--red);color:var(--white);font-family:var(--head);font-weight:600;text-align:center;line-height:1.02;border-bottom:6px solid var(--red-dark);display:flex;flex-direction:column;justify-content:center}
.tier-head.two{height:84px;font-size:25px}
.tier-head.tall{height:120px;font-size:24px}
.tier-role{font-weight:700;font-size:14px;text-align:center;margin:16px 0 18px;line-height:16px;text-decoration:underline;text-decoration-thickness:1px;text-underline-offset:3px}
.tier .perk-list{padding:0 16px 0 18px;font-size:13.5px;color:var(--text-gray);line-height:16px}
.tier .perk-list li{margin-bottom:16px}
.tier .perk-list li::before,.tier .perk-list li::after{color:var(--navy)}
.tier-note{font-size:13.5px;color:var(--text-gray);text-align:center;line-height:16px;padding:0 20px}
.row-one{top:441px;height:525px;width:232px}
.row-two{top:971px;height:360px;width:232px}
.col-1{left:28px}.col-2{left:265px}.col-3{left:504px}.col-4{left:742px}
.short{top:971px;height:225px;width:232px}
.exhibitor{position:absolute;left:265px;top:1201px;width:471px;height:128px;background:#f3f3f3;border:1px solid var(--card-edge)}
.exhibitor .tier-head{height:68px;font-size:26px}
.exhibitor .tier-note{margin-top:20px}
.ads .perk-list{font-weight:700;color:var(--ink)}
.sheet-foot{position:absolute;left:0;bottom:0;width:1000px;height:68px;background:var(--navy-deep);border-top:5px solid var(--red);color:var(--white);text-align:center;line-height:63px;font-size:18px}
.sheet-foot .url{font-size:24px;margin-left:6px}
</style>
</head>
<body>

<section class="page cover" aria-label="Summit cover page">
  <div class="brand-seal">Texas RVN</div>
  <div class="theme-line theme-power">THE POWER<span class="of">OF</span></div>
  <div class="theme-line theme-connection">CONNECTION</div>
  <div class="event-name">TEXAS RVN CONFERENCE</div>
  <div class="event-dates">APRIL 23-25</div>
  <div class="year-tab"><span>2020</span></div>
  <div class="event-venue venue-line">EARLY BIRD AND MEMBER DISCOUNTS LOCATION HARBOR LODGE</div>
  <div class="event-venue venue-city">PLAINSVIEW COUNTY</div>
  <svg class="theme-art" role="img" aria-label="Photo of two hands pulling apart a cut electrical cable with sparks of lightning between the ends" viewBox="0 0 1000 450" preserveAspectRatio="none">
    <defs>
      <radialGradient id="spark-glow" cx="50%" cy="42%" r="60%">
        <stop offset="0" stop-color="#dff3ff"/>
        <stop offset=".12" stop-color="#8fb9cf"/>
        <stop offset=".45" stop-color="#2e4857"/>
        <stop offset="1" stop-color="#0a1217" stop-opacity="0"/>
      </radialGradient>
    </defs>
    <rect width="1000" height="450" fill="url(#spark-glow)"/>
  </svg>
  <div class="sponsor-marks">
    <div class="sponsor-mark"><span class="dot"></span>The Meridale</div>
    <div class="sponsor-mark gold">Plainsview VTO</div>
  </div>
  <div class="cover-url">www.texasrvn.example</div>
</section>

<section class="page sponsor-sheet" aria-label="Sponsor opportunities">
  <svg class="top-photo" viewBox="0 0 500 430" aria-hidden="true">
    <circle cx="350" cy="150" r="300" fill="var(--navy)"/>
    <circle cx="360" cy="150" r="288" fill="#e11f26"/>
    <circle cx="372" cy="150" r="276" fill="#ffffff"/>
  </svg>
  <svg class="top-photo" role="img" aria-label="Group photo of conference team members in uniform" viewBox="0 0 500 430">
    <defs>
      <clipPath id="photo-clip"><circle cx="380" cy="150" r="268"/></clipPath>
      <linearGradient id="photo-tone" x1="0" y1="0" x2="0" y2="1">
        <stop offset="0" stop-color="#6f7a5e"/>
        <stop offset=".45" stop-color="#2b3140"/>
        <stop offset="1" stop-color="#4a4a52"/>
      </linearGradient>
    </defs>
    <rect width="500" height="430" fill="url(#photo-tone)" clip-path="url(#photo-clip)"/>
  </svg>

  <div class="champion-title">CHAMPION $10,000</div>
  <ul class="perk-list champion-perks">
    <li>Conference Sponsor</li>
    <li>Opportunity to introduce Speaker</li>
    <li>Texas RVN Association 2020 Conference<br>"your organization" on front cover<span class="presented">Presented by</span></li>
    <li>Full Page Program Ad</li>
    <li>Acknowledgments in Media Spotlight</li>
    <li>Personal Signage (color)</li>
    <li>Exhibit Booth</li>
    <li>10 Paid Registrations</li>
    <li>Sponsor Ribbons (10)</li>
    <li>Organizational Membership Texas RVN</li>
  </ul>

  <div class="tier row-one col-1">
    <div class="tier-head two">Visionary<br>$8,000</div>
    <div class="tier-role">Award Luncheon<br>Sponsor</div>
    <ul class="perk-list">
      <li>Includes Opportunity to Introduce Speaker</li>
      <li>Full Page Program Ad</li>
      <li>Acknowledgments in Media Spotlights</li>
      <li>Personalized Signage (Color)</li>
      <li>Exhibit Booth</li>
      <li>8 paid Registrations</li>
      <li>Sponsor Ribbons (8)</li>
      <li>Organizational Membership Texas RVN</li>
    </ul>
  </div>
  <div class="tier row-one col-2">
    <div class="tier-head two">Leader<br>$5,000</div>
    <div class="tier-role">Morning Plenary<br>Sponsor</div>
    <ul class="perk-list">
      <li>Includes Opportunity to Introduce Speaker</li>
      <li>Full Page Program Ad</li>
      <li>Acknowledgments in Media Spotlights</li>
      <li>Personalized Signage (Color)</li>
      <li>Exhibit Booth</li>
      <li>5 paid Registrations</li>
      <li>Sponsor Ribbons (5)</li>
      <li>Organizational Membership Texas RVN</li>
    </ul>
  </div>
  <div class="tier row-one col-3">
    <div class="tier-head two">Builder<br>$2,500</div>
    <div class="tier-role">Workshop Sponsor</div>
    <ul class="perk-list">
      <li>Includes Opportunity to Introduce Speaker</li>
      <li>Half Page Program Ad</li>
      <li>Acknowledgments in Media Spotlights</li>
      <li>Group Signage (Color)</li>
      <li>Exhibit Booth</li>
      <li>3 paid Registrations</li>
      <li>Sponsor Ribbons (3)</li>
      <li>Organizational Membership Texas RVN</li>
    </ul>
  </div>
  <div class="tier row-one col-4">
    <div class="tier-head two">Advocate<br>$1,000</div>
    <div class="tier-role">Workshop Sponsor</div>
    <ul class="perk-list">
      <li>Advocate $1,000 Workshop Sponsor</li>
      <li>Includes Opportunity to Introduce Speaker</li>
      <li>Half Page Program Ad</li>
      <li>Acknowledgments in Media Spotlights</li>
      <li>Group Signage (Color)</li>
      <li>Exhibit Booth</li>
      <li>2 paid Registrations</li>
      <li>Sponsor Ribbons (2)</li>
      <li>Organizational Membership Texas RVN</li>
    </ul>
  </div>

  <div class="tier row-two col-1">
    <div class="tier-head two">Friend<br>$500</div>
    <ul class="perk-list" style="margin-top:26px">
      <li>Company Logo</li>
      <li>Exhibit Booth</li>
      <li>1 Paid Registration</li>
      <li>Sponsor Ribbon(1)</li>
      <li>Organizational</li>
      <li>Membership to Texas RVN</li>
    </ul>
  </div>
  <div class="tier short col-2">
    <div class="tier-head tall">SPONSOR AN<br>OFFICER<br>$500</div>
    <ul class="perk-list" style="margin-top:12px">
      <li style="margin-bottom:6px">Covers conference training for one officer</li>
      <li>Company Logo and recognition in Print material</li>
    </ul>
  </div>
  <div class="tier short col-3">
    <div class="tier-head tall">Coin Sponsor<br>$1000 (only1)<br>add-on to<br>another package</div>
    <div class="tier-note" style="margin-top:26px">Conference Coin will be designed for giveaway w/ sponsor logo on the back</div>
  </div>
  <div class="tier row-two col-4 ads">
    <div class="tier-head two">Program ADS</div>
    <ul class="perk-list" style="margin-top:26px">
      <li>$250-1/4 page ad</li>
      <li>$500 &nbsp;1/2 page ad</li>
      <li>$1000 Full page ad</li>
    </ul>
  </div>
  <div class="exhibitor">
    <div class="tier-head">EXHIBITOR $250</div>
    <div class="tier-note">Exhibit Boothin in Print material</div>
  </div>

  <div class="sheet-foot">Register At: <span class="url">www.texasrvn.example</span></div>
</section>

</body>
</html>
```